Digital Menu for New Picnic Company

We're in the process of creating a new picnic business called Cedar Hollow Hampers. We need our menu created as per the content in this google doc https://files.examplecloud.net/doc/7Kq2Rv9LmTzX4bWcYhJnPaE3sUd8FgVoNiQ5rMtLyKe/view?share=link
Please look at our website www.cedarhollowhampers.com.au to get an understanding of what we do and our branding style. We need the menu to be created matching the branding/colours as per our website however other than that please feel free to design it however you like and I will provide feedback from there. We are offering a high end gourmet product so the look and feel of the menu does need to reflect this.
PLEASE NOTE: This menu will only be displayed online as a PDF and doesn't need to be printed or provided physically.

```html
<!DOCTYPE html>
<html lang="en">
<head>
<meta charset="utf-8">
<title>Cedar Hollow Hampers – Gourmet Picnic Menu</title>
<link href="https://fonts.googleapis.com/css2?family=Signika:wght@600&family=Source+Sans+3:wght@400;600&display=swap" rel="stylesheet">
<style>
:root{
  --backdrop:#bdbdbf;
  --paper:#ffffff;
  --paper-grain:#f3f4f6;
  --blue:#1fa0dc;
  --green:#6cbf45;
  --ink:#3b3b3b;
  --leader:#b8b8b8;
}
*{margin:0;padding:0;box-sizing:border-box}
html,body{width:1200px;height:632px;overflow:hidden}
body{background:var(--backdrop);font-family:"Source Sans 3",sans-serif;color:var(--ink);position:relative}
.page{position:absolute;top:75px;width:340px;height:479px;background:linear-gradient(90deg,var(--paper) 0 48%,var(--paper-grain) 49%,var(--paper) 50%) 0 0/34px 100%;background-color:var(--paper);overflow:hidden}
.page--cover{left:72px;background:var(--paper)}
.page--cheese{left:434px}
.page--extras{left:797px}

.heading{font-family:"Signika",sans-serif;font-weight:600;text-transform:uppercase;letter-spacing:.2px}
.section-title{position:absolute;color:var(--green);font-size:10.5px}
.banner{position:absolute;left:0;height:18px;background:var(--blue);color:#fff;font-size:13.5px;line-height:18px;padding-left:14px;border-radius:0 8px 0 0}

.list{position:absolute;width:114px}
.item{display:flex;align-items:flex-end;height:11.4px;font-size:7px;line-height:8px}
.item .leader{flex:1;border-bottom:1px dotted var(--leader);margin:0 3px 2px}
.item .price{color:var(--green);font-weight:600}

.badge{position:absolute;border-radius:50%;background:var(--blue);color:#fff;display:flex;flex-direction:column;align-items:center;justify-content:center;text-align:center;line-height:1;box-shadow:0 0 0 1.5px #fff,0 0 0 2.5px var(--blue)}
.badge--large{width:60px;height:60px;font-size:11.5px;left:272px;top:83px}
.badge--small{width:23px;height:23px;font-size:3.8px}

.photo{position:absolute;border-radius:1px}
.footer{position:absolute;left:0;top:370px;width:340px;height:109px}
.footer-text{position:absolute;left:0;width:340px;text-align:center;color:#fff}
.footer-address{top:438px;font-size:8.5px;font-weight:600}
.footer-links{top:456px;font-size:5.8px}

.cover-photo{position:absolute;left:0;top:0}
.brand-seal{position:absolute;left:240px;top:263px;width:84px;height:84px;border-radius:50%;background:var(--blue);box-shadow:0 0 0 2px #fff;display:flex;align-items:center;justify-content:center;text-align:center;color:#fff;font-family:"Source Sans 3",sans-serif;font-weight:600;font-size:10px;line-height:1.15;padding:8px}
.cover-title{position:absolute;top:351px;left:0;width:340px;text-align:center;color:var(--blue);font-size:16px}
.cover-copy{position:absolute;left:14px;top:376px;width:314px;font-size:6.1px;line-height:8.1px}
.cover-copy p{margin-bottom:4.5px}
</style>
</head>
<body>

<!-- Cover -->
<section class="page page--cover">
  <svg class="cover-photo" width="340" height="360" viewBox="0 0 340 360">
    <defs>
      <linearGradient id="falls" x1="0" y1="0" x2="1" y2="1">
        <stop offset="0" stop-color="#4c6b34"/>
        <stop offset=".45" stop-color="#6b5a45"/>
        <stop offset=".75" stop-color="#8a5a3c"/>
        <stop offset="1" stop-color="#c9d1d6"/>
      </linearGradient>
    </defs>
    <path role="img" aria-label="Photograph of a waterfall cascading over mossy rocks in a rainforest gorge" d="M0 0H340V290C300 318 250 330 180 325C110 320 50 315 0 350Z" fill="url(#falls)"/>
    <path d="M0 352C50 318 110 318 180 326C250 333 300 322 340 290" fill="none" stroke="var(--blue)" stroke-width="5"/>
    <path d="M0 360C40 330 100 326 170 334C250 342 305 326 340 298" fill="none" stroke="var(--green)" stroke-width="2.5"/>
  </svg>
  <div class="brand-seal">Cedar Hollow Hampers</div>
  <h1 class="heading cover-title">Gourmet Picnic Menu</h1>
  <div class="cover-copy">
    <p>Our Gourmet Picnics are handcrafted and delivered to your picnic spot on a wooden grazing tray. They come sealed in a catering box to ensure they are not tampered with. You then open the box and remove the grazing tray to enjoy the food. We prepare our food in accordance with food handling guidelines and all COVID precautions.</p>
    <p>We also provide complimentary beverages as part of the Gourmet Picnic being your choice of beers, wine or soft drink. You also can choose between still or sparkling water.</p>
    <p>As everyone has varying tastes, we have created our menu to be fully customisable so you can design your own picnic. We offer a wide variety of choices while focussing on quality ingredients for each component of your picnic.</p>
  </div>
</section>

<!-- Cheese & Dips -->
<section class="page page--cheese">
  <div class="photo" role="img" aria-label="Photograph of a cheese board with grapes, figs and brie" style="left:14px;top:19px;width:100px;height:76px;background:linear-gradient(135deg,#d8c9a8,#8c2f3a 55%,#e9e3d2)"></div>
  <div class="photo" role="img" aria-label="Photograph of crackers and blue cheese on a pale blue plate" style="left:120px;top:19px;width:100px;height:76px;background:radial-gradient(circle,#d79a4a 25%,#7fb9d6 60%,#6b4a2a)"></div>
  <div class="photo" role="img" aria-label="Photograph of a grazing platter with olives, cheeses and wine" style="left:226px;top:19px;width:100px;height:76px;background:linear-gradient(160deg,#5a4a3a,#6d3a5a 45%,#c7b79a)"></div>
  <div class="badge badge--large heading">Choose<span style="margin-top:2px">Any 2</span></div>

  <div class="banner heading" style="top:111px;width:150px">Cheese &amp; Dips</div>

  <h2 class="heading section-title" style="left:15px;top:142px">Cheeses</h2>
  <div class="list" style="left:15px;top:154px">
    <div class="item"><span>Creamy Blue</span><span class="leader"></span><span class="price">$00.00</span></div>
    <div class="item"><span>Blue Vein</span><span class="leader"></span><span class="price">$00.00</span></div>
    <div class="item"><span>Chilli Cream</span><span class="leader"></span><span class="price">$00.00</span></div>
    <div class="item"><span>Double Cream Brie</span><span class="leader"></span><span class="price">$00.00</span></div>
    <div class="item"><span>Camembert</span><span class="leader"></span><span class="price">$00.00</span></div>
    <div class="item"><span>Cheddar</span><span class="leader"></span><span class="price">$00.00</span></div>
    <div class="item"><span>Vintage Cheddar</span><span class="leader"></span><span class="price">$00.00</span></div>
    <div class="item"><span>Parmesan</span><span class="leader"></span><span class="price">$00.00</span></div>
    <div class="item"><span>Dutch Smoked</span><span class="leader"></span><span class="price">$00.00</span></div>
    <div class="item"><span>Goat Milk</span><span class="leader"></span><span class="price">$00.00</span></div>
  </div>

  <h2 class="heading section-title" style="left:189px;top:142px">Dips</h2>
  <div class="list" style="left:189px;top:154px;width:128px">
    <div class="item"><span>Mild Salsa</span><span class="leader"></span><span class="price">$00.00</span></div>
    <div class="item"><span>Spicy Salsa</span><span class="leader"></span><span class="price">$00.00</span></div>
    <div class="item"><span>Avocado</span><span class="leader"></span><span class="price">$00.00</span></div>
    <div class="item"><span>Hommus</span><span class="leader"></span><span class="price">$00.00</span></div>
    <div class="item"><span>Sweet Potato</span><span class="leader"></span><span class="price">$00.00</span></div>
    <div class="item"><span>Caramelised Onion</span><span class="leader"></span><span class="price">$00.00</span></div>
    <div class="item"><span>Roast Capsicum</span><span class="leader"></span><span class="price">$00.00</span></div>
    <div class="item"><span>Caviar</span><span class="leader"></span><span class="price">$00.00</span></div>
    <div class="item"><span>Guacamole</span><span class="leader"></span><span class="price">$00.00</span></div>
    <div class="item"><span>Sweet Chilli &amp; Sour Cream</span><span class="leader"></span><span class="price">$00.00</span></div>
    <div class="item"><span>Cashews</span><span class="leader"></span><span class="price">$00.00</span></div>
    <div class="item"><span>Jalapeno</span><span class="leader"></span><span class="price">$00.00</span></div>
  </div>

  <h2 class="heading section-title" style="left:15px;top:305px">Crackers</h2>
  <div class="list" style="left:15px;top:317px">
    <div class="item"><span>Butter Rounds</span><span class="leader"></span><span class="price">$00.00</span></div>
    <div class="item"><span>Natural Artisan Crackers</span><span class="leader"></span><span class="price">$00.00</span></div>
    <div class="item"><span>Wheat Crispbread</span><span class="leader"></span><span class="price">$00.00</span></div>
    <div class="item"><span>Flat bread</span><span class="leader"></span><span class="price">$00.00</span></div>
    <div class="item"><span>Chilli jam flat bread</span><span class="leader"></span><span class="price">$00.00</span></div>
    <div class="item"><span>Assorted crackers</span><span class="leader"></span><span class="price">$00.00</span></div>
    <div class="item"><span>Veggie crackers</span><span class="leader"></span><span class="price">$00.00</span></div>
  </div>
  <div class="list" style="left:189px;top:317px;width:128px">
    <div class="item"><span>Pita Crackers</span><span class="leader"></span><span class="price">$00.00</span></div>
    <div class="item"><span>Bread Sticks</span><span class="leader"></span><span class="price">$00.00</span></div>
    <div class="item"><span>Corn Chips</span><span class="leader"></span><span class="price">$00.00</span></div>
    <div class="item"><span>Bruschetta Toasts</span><span class="leader"></span><span class="price">$00.00</span></div>
    <div class="item"><span>Wafer Crackers</span><span class="leader"></span><span class="price">$00.00</span></div>
    <div class="item"><span>Rice Crackers</span><span class="leader"></span><span class="price">$00.00</span></div>
  </div>

  <svg class="footer" viewBox="0 0 340 109">
    <path d="M0 72C40 40 90 36 170 34C260 32 318 26 340 -6" fill="none" stroke="var(--green)" stroke-width="3"/>
    <path d="M0 109V78C40 47 90 42 170 40C260 38 320 32 340 4V109Z" fill="var(--blue)"/>
  </svg>
  <div class="footer-text footer-address">PO Box 1180 Larchfield NSW 2790</div>
  <div class="footer-text footer-links">www.cedarhollowhampers.com.au &nbsp;|&nbsp; info@cedarhollowhampers.com.au</div>
</section>

<!-- Fruit, Chocolates & Beverages -->
<section class="page page--extras">
  <h2 class="heading section-title" style="left:15px;top:18px">Fruit</h2>
  <div class="badge badge--small heading" style="left:123px;top:9px">Choose<span>Any 3</span></div>
  <div class="list" style="left:15px;top:31px">
    <div class="item"><span>Strawberrys</span><span class="leader"></span><span class="price">$00.00</span></div>
    <div class="item"><span>Grapes</span><span class="leader"></span><span class="price">$00.00</span></div>
    <div class="item"><span>Passion Fruit</span><span class="leader"></span><span class="price">$00.00</span></div>
    <div class="item"><span>Oranges</span><span class="leader"></span><span class="price">$00.00</span></div>
    <div class="item"><span>Kiwi Fruit</span><span class="leader"></span><span class="price">$00.00</span></div>
  </div>

  <h2 class="heading section-title" style="left:189px;top:18px">Chocolates</h2>
  <div class="badge badge--small heading" style="left:303px;top:9px">Choose<span>Any 1</span></div>
  <div class="list" style="left:189px;top:31px;width:128px">
    <div class="item"><span>Hazel Crest Truffles</span><span class="leader"></span><span class="price">$00.00</span></div>
    <div class="item"><span>Alpine Peak Bar</span><span class="leader"></span><span class="price">$00.00</span></div>
    <div class="item"><span>Velour Truffle Balls</span><span class="leader"></span><span class="price">$00.00</span></div>
    <div class="item"><span>Rocky Road</span><span class="leader"></span><span class="price">$00.00</span></div>
    <div class="item"><span>Crisp Wafer Fingers</span><span class="leader"></span><span class="price">$00.00</span></div>
    <div class="item"><span>Malt Puffs</span><span class="leader"></span><span class="price">$00.00</span></div>
    <div class="item"><span>Dairy Meadow Chocolate</span><span class="leader"></span><span class="price">$00.00</span></div>
  </div>

  <div class="banner heading" style="top:123px;width:225px">Complimentary Beverages</div>

  <h2 class="heading section-title" style="left:15px;top:149px;font-size:9px">Water Preference</h2>
  <div class="list" style="left:15px;top:157px">
    <div class="item"><span>Still</span><span class="leader"></span><span class="price">$00.00</span></div>
    <div class="item"><span>Sparkling</span><span class="leader"></span><span class="price">$00.00</span></div>
    <div class="item"><span>Still &amp; Sparkling</span><span class="leader"></span><span class="price">$00.00</span></div>
  </div>

  <h2 class="heading section-title" style="left:15px;top:209px;font-size:9px">Wine</h2>
  <div class="badge badge--small heading" style="left:123px;top:198px">Choose<span>Any 2</span></div>
  <div class="list" style="left:15px;top:218px">
    <div class="item"><span>Champagne</span><span class="leader"></span><span class="price">$00.00</span></div>
    <div class="item"><span>Sauvignon Blanc</span><span class="leader"></span><span class="price">$00.00</span></div>
    <div class="item"><span>Chadonnay</span><span class="leader"></span><span class="price">$00.00</span></div>
    <div class="item"><span>Malbec</span><span class="leader"></span><span class="price">$00.00</span></div>
    <div class="item"><span>Shiraz</span><span class="leader"></span><span class="price">$00.00</span></div>
    <div class="item"><span>Cabernet Sauvignon</span><span class="leader"></span><span class="price">$00.00</span></div>
    <div class="item"><span>Merlot</span><span class="leader"></span><span class="price">$00.00</span></div>
  </div>

  <h2 class="heading section-title" style="left:15px;top:312px;font-size:9px">Beer</h2>
  <div class="list" style="left:15px;top:319px">
    <div class="item"><span>Craft Lager</span><span class="leader"></span><span class="price">$00.00</span></div>
    <div class="item"><span>Craft Pale Ale</span><span class="leader"></span><span class="price">$00.00</span></div>
    <div class="item"><span>Craft XPA</span><span class="leader"></span><span class="price">$00.00</span></div>
    <div class="item"><span>Australian Lager</span><span class="leader"></span><span class="price">$00.00</span></div>
    <div class="item"><span>Australian Dry</span><span class="leader"></span><span class="price">$00.00</span></div>
    <div class="item"><span>International Lager</span><span class="leader"></span><span class="price">$00.00</span></div>
    <div class="item"><span>Cider</span><span class="leader"></span><span class="price">$00.00</span></div>
  </div>

  <h2 class="heading section-title" style="left:189px;top:149px;font-size:9px">Non Alcoholic</h2>
  <div class="list" style="left:189px;top:157px;width:128px">
    <div class="item"><span>Classic Cola</span><span class="leader"></span><span class="price">$00.00</span></div>
    <div class="item"><span>Cola No Sugar</span><span class="leader"></span><span class="price">$00.00</span></div>
    <div class="item"><span>Diet Cola</span><span class="leader"></span><span class="price">$00.00</span></div>
    <div class="item"><span>Cola Caffeine Free</span><span class="leader"></span><span class="price">$00.00</span></div>
    <div class="item"><span>Vanilla Cola</span><span class="leader"></span><span class="price">$00.00</span></div>
    <div class="item"><span>Blue Cap Cola</span><span class="leader"></span><span class="price">$00.00</span></div>
    <div class="item"><span>Blue Cap Max</span><span class="leader"></span><span class="price">$00.00</span></div>
    <div class="item"><span>Blue Cap Max Vanilla</span><span class="leader"></span><span class="price">$00.00</span></div>
    <div class="item"><span>Fizz Lemon Lime</span><span class="leader"></span><span class="price">$00.00</span></div>
    <div class="item"><span>Orange Burst</span><span class="leader"></span><span class="price">$00.00</span></div>
    <div class="item"><span>Citrus Peak</span><span class="leader"></span><span class="price">$00.00</span></div>
    <div class="item"><span>Lemon Squash</span><span class="leader"></span><span class="price">$00.00</span></div>
    <div class="item"><span>Lemon Squash Zero</span><span class="leader"></span><span class="price">$00.00</span></div>
    <div class="item"><span>Sunny Orange</span><span class="leader"></span><span class="price">$00.00</span></div>
    <div class="item"><span>Sunny Orange Zero</span><span class="leader"></span><span class="price">$00.00</span></div>
    <div class="item"><span>Apple Cider</span><span class="leader"></span><span class="price">$00.00</span></div>
    <div class="item"><span>Ginger Beer</span><span class="leader"></span><span class="price">$00.00</span></div>
    <div class="item"><span>Diet Ginger Beer</span><span class="leader"></span><span class="price">$00.00</span></div>
    <div class="item"><span>Lemon Lime &amp; Bitters</span><span class="leader"></span><span class="price">$00.00</span></div>
    <div class="item"><span>Creaming Soda</span><span class="leader"></span><span class="price">$00.00</span></div>
    <div class="item"><span>Sugar Free Creaming Soda</span><span class="leader"></span><span class="price">$00.00</span></div>
  </div>

  <svg class="footer" viewBox="0 0 340 109">
    <path d="M0 72C40 40 90 36 170 34C260 32 318 26 340 -6" fill="none" stroke="var(--green)" stroke-width="3"/>
    <path d="M0 109V78C40 47 90 42 170 40C260 38 320 32 340 4V109Z" fill="var(--blue)"/>
  </svg>
  <div class="footer-text footer-address">PO Box 1180 Larchfield NSW 2790</div>
  <div class="footer-text footer-links">www.cedarhollowhampers.com.au &nbsp;|&nbsp; info@cedarhollowhampers.com.au</div>
</section>

</body>
</html>
```